Company Capability Brochure

Want to create a mulit paged brochure to hand out to potential clients to show our services and capabilities.

Attached is a rough draft we made using chatgpt which can be use as an example and includes the categories, text, our logo and preferred colour scheme we wish to use.
Would like to make this more look more visually appealing and a more professional layout over more pages.

```html
<!DOCTYPE html>
<html lang="en">
<head>
<meta charset="utf-8">
<title>Vigilant Guard Systems – Capability Brochure</title>
<link href="https://fonts.googleapis.com/css2?family=Poppins:wght@400;500;600&display=swap" rel="stylesheet">
<style>
  :root{
    --navy:#1c1a6b;
    --navy-deep:#141250;
    --indigo:#2a2890;
    --cyan:#1fb4ea;
    --blue:#1565c8;
    --bright-blue:#1e88e5;
    --white:#ffffff;
    --ink:#111111;
    --page:#ffffff;
  }
  *{box-sizing:border-box;margin:0;padding:0}
  html,body{width:1200px;height:2720px;overflow:hidden;background:var(--page)}
  body{position:relative;font-family:"Poppins",sans-serif;color:var(--white)}

  .spread{position:absolute;left:76px;width:1049px;height:810px;box-shadow:0 10px 30px rgba(0,0,0,.18)}
  .spread--outside{top:71px}
  .spread--inside{top:1831px}

  .panel{position:absolute;top:0;height:810px;overflow:hidden;
    background:linear-gradient(180deg,var(--navy-deep) 0%,var(--navy) 55%,var(--indigo) 100%)}
  .panel--left{left:0;width:345px}
  .panel--middle{left:345px;width:352px}
  .panel--right{left:697px;width:352px}

  .strip-top-white{position:absolute;left:0;top:0;width:100%;height:24px;background:var(--white)}
  .strip-top-blue{position:absolute;left:0;top:0;width:100%;height:24px;background:linear-gradient(90deg,var(--blue),var(--cyan))}
  .strip-bottom-blue{position:absolute;left:0;bottom:0;width:100%;height:24px;background:linear-gradient(90deg,var(--blue),var(--cyan))}
  .strip-bottom-white{position:absolute;left:0;bottom:0;width:100%;height:24px;background:var(--white)}

  .photo{position:absolute}

  .heading{position:absolute;color:var(--cyan);font-weight:500;font-size:25px;line-height:24px}

  /* services */
  .service-list{position:absolute;left:24px;top:271px;list-style:none}
  .service{display:flex;align-items:center;width:195px;height:34px;margin-bottom:7px;
    border:1.5px solid #3d5cc8;border-left:none;border-radius:0 5px 5px 0;font-weight:500;font-size:18px}
  .service .icon{width:32px;height:32px;background:var(--white);border-radius:3px;margin-right:13px;display:flex;align-items:center;justify-content:center;flex-shrink:0}

  .client-box{position:absolute;left:17px;top:554px;width:285px;height:207px;border:1.5px solid #3d5cc8;border-left:none;border-radius:0 14px 14px 0;padding:8px 0 0 7px}
  .client-list{list-style:none;font-size:15.5px;line-height:19px}
  .client-list li::before{content:"";display:inline-block;width:8px;height:2px;background:var(--cyan);margin-right:6px;vertical-align:middle}

  /* contact */
  .contact-tab{position:absolute;left:0;top:412px;width:181px;height:36px;background:var(--white);color:var(--cyan);font-size:24px;font-weight:500;padding-left:24px;line-height:38px}
  .contact-company{position:absolute;left:24px;top:476px;font-size:15.5px;line-height:17px}
  .contact-list{position:absolute;left:24px;top:535px;list-style:none;font-size:15.5px}
  .contact-item{display:flex;align-items:flex-start;margin-bottom:12px;line-height:17px}
  .contact-item .icon{width:27px;height:27px;background:var(--white);border-radius:4px;margin-right:9px;display:flex;align-items:center;justify-content:center;flex-shrink:0}
  .contact-item span{padding-top:5px}
  .contact-item.phone span{font-weight:600}
  .cta-box{position:absolute;left:24px;top:705px;width:276px;height:62px;border:1.5px solid var(--white);border-left:none;border-radius:0 10px 10px 0;color:var(--cyan);font-size:22px;line-height:24px;font-weight:500;padding-top:6px}

  /* cover */
  .cover-brand{position:absolute;left:741px;top:160px;width:300px;text-align:center;color:var(--blue);font-weight:600;letter-spacing:3px}
  .cover-brand .name-main{display:block;font-size:34px;line-height:38px}
  .cover-brand .name-sub{display:block;font-size:17px;line-height:24px;letter-spacing:5px}
  .cover-tagline{position:absolute;left:741px;top:286px;width:240px;text-align:center;color:var(--cyan);font-size:23px;line-height:25px;font-weight:500}

  /* inside */
  .statement-head{position:absolute;display:flex;align-items:center}
  .statement-head .heading{position:static;font-size:25px;line-height:23px;margin-left:14px}
  .statement-body{position:absolute;font-size:16px;line-height:19px}
</style>
</head>
<body>

<!-- OUTSIDE SPREAD -->
<section class="spread spread--outside" aria-label="Brochure outside">
  <div class="panel panel--left">
    <div class="photo" role="img" aria-label="Illustration of a glowing security shield with network icons around it"
      style="left:0;top:24px;width:345px;height:190px;background:radial-gradient(ellipse at 55% 45%,#2a8fd6 0%,#1f4fa8 35%,rgba(28,26,107,0) 75%)"></div>
    <div class="strip-top-white"></div>
    <h2 class="heading" style="left:25px;top:206px">Our<br>Services</h2>
    <ul class="service-list">
      <li class="service"><span class="icon"><svg width="20" height="20" viewBox="0 0 20 20"><rect x="2" y="5" width="12" height="7" rx="1" fill="var(--blue)"/><rect x="14" y="7" width="3" height="3" fill="var(--blue)"/><rect x="5" y="12" width="2" height="5" fill="var(--blue)"/></svg></span>CCTV Systems</li>
      <li class="service"><span class="icon"><svg width="20" height="20" viewBox="0 0 20 20"><rect x="4" y="2" width="10" height="16" rx="1" fill="none" stroke="var(--blue)" stroke-width="2"/><circle cx="9" cy="7" r="2" fill="var(--blue)"/><path d="M16 8q2 2 0 4" stroke="var(--blue)" fill="none" stroke-width="1.5"/></svg></span>Access Control</li>
      <li class="service"><span class="icon"><svg width="20" height="20" viewBox="0 0 20 20"><rect x="4" y="2" width="9" height="16" rx="1" fill="none" stroke="var(--blue)" stroke-width="2"/><circle cx="8.5" cy="12" r="2" fill="var(--blue)"/><path d="M15 7q2 3 0 6" stroke="var(--blue)" fill="none" stroke-width="1.5"/></svg></span>Intercoms</li>
      <li class="service"><span class="icon"><svg width="20" height="20" viewBox="0 0 20 20"><path d="M10 3a5 5 0 0 1 5 5v5l2 2H3l2-2V8a5 5 0 0 1 5-5z" fill="var(--blue)"/><circle cx="10" cy="17" r="1.6" fill="var(--blue)"/></svg></span>Alarms</li>
      <li class="service"><span class="icon"><svg width="20" height="20" viewBox="0 0 20 20"><path d="M3 4h14M3 17h14M5 4v13M8.5 4v13M11.5 4v13M15 4v13" stroke="var(--blue)" stroke-width="1.8" fill="none"/></svg></span>Gates</li>
    </ul>
    <h2 class="heading" style="left:25px;top:496px">Our<br>Clients</h2>
    <div class="client-box">
      <ul class="client-list">
        <li>Riverside Grand Hotel</li>
        <li>Parkview Suites Hotel</li>
        <li>Meridian College</li>
        <li>Summit Body Corporate</li>
        <li>Hale &amp; Morton</li>
        <li>Strata Plus</li>
        <li>KTLG</li>
        <li>Coastal Strata</li>
        <li>Westbrook Rugby League Club</li>
        <li>Ellisons</li>
      </ul>
    </div>
    <div class="strip-bottom-blue"></div>
  </div>

  <div class="panel panel--middle">
    <div class="strip-top-blue"></div>
    <div class="photo" role="img" aria-label="Photo of a security officer with a radio watching a wall of CCTV monitors"
      style="left:0;top:24px;width:352px;height:335px;background:linear-gradient(160deg,#6d6d70 0%,#2e2e33 40%,#111114 100%)"></div>
    <div class="photo" style="left:0;top:359px;width:352px;height:14px;background:linear-gradient(90deg,var(--blue),var(--bright-blue))"></div>
    <div class="contact-tab">Contact Us</div>
    <p class="contact-company">Vigilant<br>Guard Systems</p>
    <ul class="contact-list">
      <li class="contact-item phone"><span class="icon"><svg width="16" height="16" viewBox="0 0 16 16"><path d="M3 1l3 3-1.5 2a9 9 0 0 0 5.5 5.5L12 10l3 3-2 2C7 15 1 9 1 3z" fill="var(--blue)"/></svg></span><span>1300 555 018</span></li>
      <li class="contact-item"><span class="icon"><svg width="16" height="16" viewBox="0 0 16 16"><rect x="1" y="3" width="14" height="10" fill="var(--blue)"/><path d="M1 3l7 6 7-6" stroke="#fff" fill="none" stroke-width="1.3"/></svg></span><span>hello@vigilantguard.com.au</span></li>
      <li class="contact-item"><span class="icon"><svg width="16" height="16" viewBox="0 0 16 16"><circle cx="8" cy="8" r="6.5" fill="none" stroke="var(--blue)" stroke-width="1.4"/><path d="M1.5 8h13M8 1.5q-4 6.5 0 13M8 1.5q4 6.5 0 13" stroke="var(--blue)" fill="none" stroke-width="1.2"/></svg></span><span>www.vigilantguard.com.au</span></li>
      <li class="contact-item"><span class="icon"><svg width="16" height="16" viewBox="0 0 16 16"><path d="M8 1a5 5 0 0 1 5 5c0 4-5 9-5 9S3 10 3 6a5 5 0 0 1 5-5z" fill="var(--blue)"/><circle cx="8" cy="6" r="2" fill="#fff"/></svg></span><span>12/8 Harbour Rd, Northvale,<br>NSW 2199</span></li>
    </ul>
    <p class="cta-box">Be Informed and Make<br>The Right Choice</p>
    <div class="strip-bottom-white"></div>
  </div>

  <div class="panel panel--right">
    <div class="photo" role="img" aria-label="Photo of wall-mounted CCTV security cameras"
      style="left:0;top:0;width:352px;height:810px;background:radial-gradient(ellipse at 65% 65%,#8a95b8 0%,#3a4c8f 30%,#1e2470 65%,var(--navy-deep) 100%)"></div>
    <div class="strip-bottom-blue"></div>
  </div>

  <svg class="cover-shield" width="1049" height="810" viewBox="0 0 1049 810" style="position:absolute;left:0;top:0" aria-hidden="true">
    <defs>
      <clipPath id="shield-inner"><path d="M842 0Q778 52 656 88L656 296Q676 372 866 438Q1032 380 1049 322L1049 0Z"/></clipPath>
    </defs>
    <path d="M826 0Q762 42 641 76L641 300Q660 384 866 452Q1040 392 1049 334L1049 0Z" fill="var(--bright-blue)"/>
    <path d="M842 0Q778 52 656 88L656 296Q676 372 866 438Q1032 380 1049 322L1049 0Z" fill="var(--white)"/>
    <rect x="640" y="281" width="420" height="92" fill="#000" clip-path="url(#shield-inner)"/>
  </svg>
  <p class="cover-brand"><span class="name-main">VIGILANT</span><span class="name-sub">Guard Systems</span></p>
  <p class="cover-tagline">Be Informed<br>and Make The<br>Right Choice</p>
</section>

<!-- INSIDE SPREAD -->
<section class="spread spread--inside" aria-label="Brochure inside">
  <div class="panel panel--left">
    <div class="photo" role="img" aria-label="Photo of a dart hitting the bullseye of a dartboard"
      style="left:0;top:420px;width:345px;height:366px;background:radial-gradient(ellipse at 55% 85%,#e8e6e2 0%,#8e8c96 25%,#3a3a6e 55%,rgba(28,26,107,0) 85%)"></div>
    <div class="strip-top-white"></div>
    <div class="statement-head" style="left:24px;top:50px">
      <svg width="64" height="62" viewBox="0 0 64 62" aria-hidden="true"><rect x="16" y="2" width="44" height="56" rx="3" fill="none" stroke="var(--white)" stroke-width="2.5"/><path d="M26 14h26M26 22h26M30 34h22M30 42h22" stroke="var(--cyan)" stroke-width="3"/><circle cx="14" cy="44" r="11" fill="none" stroke="var(--cyan)" stroke-width="3"/><circle cx="14" cy="44" r="4" fill="var(--white)"/></svg>
      <h2 class="heading">Mission<br>Statement</h2>
    </div>
    <p class="statement-body" style="left:24px;top:138px;width:312px">Our mission is to deliver exceptional service and cutting-edge Electronic and Mechanical Security Solutions that not only meet but consistently exceed our clients' expectations. We are dedicated to ensuring the safety, protection, and peace of mind of those we serve by combining advanced technologies, industry expertise, and a relentless focus on quality, reliability, and customer satisfaction. Through personalized solutions, responsive support, and continuous innovation, we aim to build long-term partnerships and be a trusted name in security.</p>
    <div class="strip-bottom-blue"></div>
  </div>

  <div class="panel panel--middle">
    <div class="photo" role="img" aria-label="Close-up photo of an eye under a digital scanning overlay"
      style="left:0;top:24px;width:352px;height:380px;background:radial-gradient(ellipse at 50% 40%,#5fb8e8 0%,#3a6a9a 25%,#4a4a62 45%,rgba(28,26,107,0) 85%)"></div>
    <div class="strip-top-blue"></div>
    <div class="statement-head" style="left:24px;top:410px">
      <svg width="64" height="64" viewBox="0 0 64 64" aria-hidden="true"><rect x="14" y="4" width="40" height="56" rx="3" fill="none" stroke="var(--cyan)" stroke-width="2.5"/><path d="M22 16h12M22 26h24M22 34h24M22 42h24M22 50h16" stroke="var(--white)" stroke-width="2.5"/><ellipse cx="44" cy="16" rx="8" ry="5" fill="none" stroke="var(--white)" stroke-width="2"/><circle cx="44" cy="16" r="2" fill="var(--cyan)"/></svg>
      <h2 class="heading">Vision<br>Statement</h2>
    </div>
    <p class="statement-body" style="left:24px;top:505px;width:310px">Our vision is to be the most trusted, innovative, and customer-focused partner in the security industry, renowned for the professional installation, service, and maintenance of Electronic and Mechanical Security Systems. We strive to set the benchmark for excellence by delivering tailored, reliable, and future-ready solutions that protect what matters most to our clients, while building lasting relationships based on integrity, responsiveness, and continuous improvement.</p>
    <div class="strip-bottom-white"></div>
  </div>

  <div class="panel panel--right">
    <div class="photo" role="img" aria-label="Digital illustration of a glowing padlock inside a circuit shield"
      style="left:0;top:580px;width:352px;height:206px;background:radial-gradient(ellipse at 50% 45%,#3fa9e8 0%,#1f5db8 35%,rgba(28,26,107,0) 75%)"></div>
    <div class="strip-top-white"></div>
    <div class="statement-head" style="left:24px;top:48px">
      <svg width="56" height="62" viewBox="0 0 56 62" aria-hidden="true"><rect x="10" y="4" width="38" height="54" rx="3" fill="none" stroke="var(--white)" stroke-width="2.5"/><path d="M18 30h22M18 38h22M18 46h22" stroke="var(--white)" stroke-width="2"/><path d="M29 10l7 3v5q0 5-7 8q-7-3-7-8v-5z" fill="none" stroke="var(--cyan)" stroke-width="2"/></svg>
      <h2 class="heading">Culture<br>Statement</h2>
    </div>
    <p class="statement-body" style="left:24px;top:126px;width:312px">At the heart of our company is a culture driven by trust, innovation, and service excellence. We are a team of dedicated professionals who take pride in protecting what matters most to our clients through advanced Electronic and Mechanical Security Solutions. We cultivate a work environment built on integrity, mutual respect, and accountability, where every team member is empowered to grow, contribute ideas, and take ownership of outcomes. Collaboration, continuous improvement, and a commitment to exceeding expectations define how we operate-both with our clients and each other. We embrace change, champion innovation, and remain agile in an evolving industry-always striving to deliver smarter, more reliable, and more secure solutions. Together, we are building not just systems, but lasting partnerships and a safer future.</p>
    <div class="strip-bottom-blue"></div>
  </div>
</section>

</body>
</html>
```